Corporate Identity,Logo,Clothing,Letterhead,Business Cards,Signage etc

Name of Business - Kellaway & Brune Crash Repairs
Colours - Royal Blue, White & Yellow

Industry/Entity Type

Business

```html
<!DOCTYPE html>
<html lang="en">
<head>
<meta charset="utf-8">
<title>Kellaway &amp; Brune Crash Repairs – Business Card</title>
<link rel="stylesheet" href="https://fonts.googleapis.com/css2?family=Sorts+Mill+Goudy&display=swap">
<style>
  :root {
    --royal-blue: #1030e0;
    --faint-blue: #d4d8f6;
    --card-white: #fdfbfd;
    --page-white: #ffffff;
    --brand-yellow: #f7d21a;
  }
  * { margin: 0; padding: 0; box-sizing: border-box; }
  html, body {
    width: 1200px;
    height: 1000px;
    overflow: hidden;
    background: var(--page-white);
  }
  .canvas {
    position: relative;
    width: 1200px;
    height: 1000px;
  }
  .business-card {
    position: absolute;
    left: 210px;
    top: 365px;
    width: 780px;
    height: 270px;
    background: var(--card-white);
    border: 1px solid #ececf0;
    font-family: "Sorts Mill Goudy", Georgia, serif;
  }
  .brand-mark {
    position: absolute;
    left: 210px;
    top: 40px;
    width: 110px;
    height: 110px;
    border-radius: 50%;
    background: var(--royal-blue);
    box-shadow: 0 0 0 9px var(--brand-yellow);
  }
  .brand-name {
    position: absolute;
    left: 40px;
    top: 170px;
    width: 430px;
    text-align: center;
    color: var(--royal-blue);
    font-size: 34px;
    line-height: 1.05;
    letter-spacing: -0.5px;
  }
  .tagline {
    position: absolute;
    left: 505px;
    top: 62px;
    color: var(--royal-blue);
    font-size: 27px;
    line-height: 1.05;
    letter-spacing: -0.6px;
    transform: rotate(2deg);
    transform-origin: left top;
  }
  .watermark-mark {
    position: absolute;
    left: 605px;
    top: 125px;
    width: 70px;
    height: 70px;
    border-radius: 50%;
    background: var(--faint-blue);
  }
  .watermark-name {
    position: absolute;
    left: 480px;
    top: 205px;
    width: 290px;
    text-align: center;
    color: var(--faint-blue);
    font-size: 24px;
    line-height: 1.05;
  }
</style>
</head>
<body>
  <main class="canvas">
    <section class="business-card">
      <div class="brand-mark"></div>
      <p class="brand-name">Kellaway &amp; Brune<br>Crash Repairs</p>
      <p class="tagline">Let us Help You<br>Contact us today</p>
      <div class="watermark-mark"></div>
      <p class="watermark-name">Kellaway &amp; Brune<br>Crash Repairs</p>
    </section>
  </main>
</body>
</html>
```